Wordpress Web Design for Coach/Consultant

I need a website for my business consulting and life coaching website.
Fully responsive website built on the WordPress self-hosted content management system
CMS Installation
Fully customized graphics and design
Customized slideshow presentation slides
Up to ten main navigation content tabs
SEO optimization
Contact form configuration
Customized favicon and social media icons
Photo gallery creation
Customized portfolio
Social media integration
Blog integration
Content sharing buttons
Subscription signup integration

Target Market(s)

Women Entrepreneurs

Industry/Entity Type

Life Coaching

Number of Pages Required

5+ page

Font styles to use
Sans Serif
Decorative

Colors
ec1f27
ffffff
000000

Requirements
Must have
• Fully responsive website built on the WordPress self-hosted content management system
• CMS Installation
• Fully customized graphics and design
• Customized slideshow presentation slides
• Up to ten main navigation content tabs
• SEO optimization
• Contact form configuration
• Customized favicon and social media icons
• Photo gallery creation
• Customized portfolio
• Social media integration
• Blog integration
• Content sharing buttons
• Subscription signup integration
Nice to have
• Here are a few sample websites to take a look at:
• www.corvalyndetrie.com

```html
<!DOCTYPE html>
<html lang="en">
<head>
<meta charset="utf-8">
<title>Marisel — Business Consulting &amp; Life Coaching</title>
<link rel="stylesheet" href="https://fonts.googleapis.com/css2?family=Open+Sans:wght@400;600;700&family=Playfair+Display:wght@400;700&display=swap">
<style>
  :root {
    --page: #efefef;
    --panel: #ffffff;
    --rose: #e8506b;
    --rose-light: #f07a8f;
    --plum: #5c2268;
    --plum-dark: #44184e;
    --ink: #3a3a3a;
    --text: #7a7a7a;
    --rule: #dddddd;
    --footer: #2c2c2c;
    --footer-deep: #1f1f1f;
  }
  * { box-sizing: border-box; margin: 0; padding: 0; }
  html, body { width: 831px; height: 1200px; overflow: hidden; }
  body {
    position: relative;
    background: var(--page);
    font-family: "Open Sans", Arial, sans-serif;
    color: var(--text);
    font-size: 8px;
    line-height: 1.55;
  }
  .site { position: absolute; left: 116px; top: 0; width: 599px; height: 1075px; background: var(--panel); }
  .abs { position: absolute; }

  /* header */
  .brand { left: 116px; top: 28px; font-family: "Playfair Display", Georgia, serif; font-size: 36px; color: var(--rose); }
  .search { left: 600px; top: 46px; width: 115px; height: 20px; border: 1px solid var(--rule); background: #fafafa; display: flex; align-items: center; justify-content: space-between; padding: 0 6px; color: #aaa; font-size: 7px; }

  /* navigation */
  .main-nav { left: 116px; top: 86px; width: 599px; height: 26px; background: linear-gradient(#f06d85, var(--rose)); display: flex; }
  .main-nav a { color: #fff; text-decoration: none; font-size: 8.5px; font-weight: 600; letter-spacing: .3px; padding: 0 14px; line-height: 26px; }
  .main-nav a.active { background: var(--plum); padding: 0 16px; }

  /* hero */
  .hero { left: 116px; top: 112px; width: 599px; height: 253px; background: linear-gradient(100deg, #f6f3f2 0%, #eae4e2 45%, #d9cfcc 70%, #c9bdb8 100%); }
  .hero-title { left: 150px; top: 190px; font-family: "Playfair Display", Georgia, serif; color: var(--plum); line-height: 1.15; }
  .hero-title .line1 { font-size: 23px; display: block; }
  .hero-title .divider { display: block; width: 40px; height: 2px; background: var(--rose); margin: 8px 0; }
  .hero-title .line2 { font-size: 27px; display: block; }

  /* purple band */
  .band { left: 105px; top: 365px; width: 621px; height: 62px; background: linear-gradient(90deg, var(--plum-dark), #7a2f86 60%, var(--plum)); }
  .band-title { left: 150px; top: 382px; color: #fff; font-size: 13px; font-weight: 600; letter-spacing: .4px; }
  .band-sub { left: 150px; top: 401px; color: #e6cfe9; font-size: 8px; }
  .band-field { top: 386px; height: 20px; background: #fff; border-radius: 2px; color: #aaa; font-size: 7px; padding: 0 6px; line-height: 20px; }
  .band-go { left: 655px; top: 382px; width: 28px; height: 28px; border-radius: 50%; background: var(--rose); }

  /* content */
  .section-title { font-size: 13px; font-weight: 700; color: var(--ink); letter-spacing: .3px; }
  .accent-title { font-size: 11px; font-weight: 700; color: var(--rose); letter-spacing: .4px; border-bottom: 1px solid var(--rule); padding-bottom: 4px; }
  .welcome { left: 116px; top: 446px; width: 414px; }
  .welcome p { margin-top: 8px; }
  .blog-head { left: 116px; top: 583px; width: 414px; }

  .post { left: 116px; width: 414px; height: 130px; display: flex; gap: 18px; }
  .post-thumb { width: 174px; height: 120px; flex: none; }
  .post-body h3 { font-size: 11px; font-weight: 600; color: var(--ink); line-height: 1.3; margin: 8px 0 5px; }
  .read-more { display: inline-block; margin-top: 6px; color: var(--rose); font-weight: 700; font-size: 7px; letter-spacing: .4px; }

  /* sidebar */
  .side-photo { left: 555px; top: 450px; width: 160px; height: 105px; background: linear-gradient(135deg, #e9e2df, #cdbfb9); }
  .about-box { left: 555px; top: 555px; width: 160px; height: 92px; background: #333; color: #bbb; padding: 10px 10px; }
  .about-box h4 { color: #fff; font-size: 10px; letter-spacing: .5px; margin-bottom: 4px; }
  .gallery-head { left: 555px; top: 660px; width: 160px; }
  .gallery { left: 555px; top: 684px; width: 160px; display: grid; grid-template-columns: repeat(3, 1fr); gap: 4px; }
  .gallery span { height: 44px; display: block; }
  .news-head { left: 555px; top: 798px; width: 160px; }
  .news-text { left: 555px; top: 820px; width: 160px; }
  .news-field { left: 555px; width: 160px; height: 18px; border: 1px solid var(--rule); background: #fafafa; color: #aaa; font-size: 7px; padding: 0 6px; line-height: 16px; }
  .subscribe { left: 555px; top: 893px; width: 68px; height: 20px; background: var(--rose); color: #fff; font-size: 7.5px; font-weight: 700; text-align: center; line-height: 20px; letter-spacing: .4px; }
  .testi-head { left: 555px; top: 930px; width: 160px; }
  .testi-text { left: 555px; top: 952px; width: 160px; font-style: italic; }
  .testi-author { left: 555px; top: 1040px; font-size: 7px; color: var(--ink); font-weight: 600; }

  /* footer */
  .footer { left: 0; top: 1075px; width: 831px; height: 95px; background: var(--footer); }
  .footer-nav { left: 116px; top: 1110px; display: flex; gap: 10px; color: #ddd; font-size: 8px; font-weight: 600; }
  .socials { left: 636px; top: 1104px; display: flex; gap: 5px; }
  .socials span { width: 17px; height: 17px; border-radius: 50%; display: block; }
  .copyright-bar { left: 0; top: 1170px; width: 831px; height: 30px; background: var(--footer-deep); }
  .copyright { left: 116px; top: 1180px; color: #888; font-size: 7px; }
</style>
</head>
<body>
  <div class="site"></div>

  <header>
    <div class="abs brand">Marisel</div>
    <div class="abs search"><span>Search</span>
      <svg width="9" height="9" viewBox="0 0 10 10"><circle cx="4" cy="4" r="3" fill="none" stroke="#999" stroke-width="1.3"/><line x1="6.2" y1="6.2" x2="9" y2="9" stroke="#999" stroke-width="1.3"/></svg>
    </div>
    <nav class="abs main-nav">
      <a class="active">HOME</a><a>ABOUT</a><a>CONSULTING</a><a>COACHING</a><a>BLOG</a><a>GALLERY</a><a>CONTACT</a>
    </nav>
  </header>

  <section>
    <div class="abs hero" role="img" aria-label="Slideshow photo of a smiling woman in a grey sweater holding a white coffee cup in a bright room"></div>
    <h1 class="abs hero-title"><span class="line1">BUSINESS CONSULTING &amp;</span><span class="divider"></span><span class="line2">LIFE COACHING</span></h1>

    <div class="abs band"></div>
    <div class="abs band-title">FUSCE ULTRICIES FEUGIAT SUSCIPIT</div>
    <div class="abs band-sub">Pellentesque faucibus id accumsan ultrices sed</div>
    <div class="abs band-field" style="left:475px;width:82px">Your name</div>
    <div class="abs band-field" style="left:563px;width:82px">Your email</div>
    <div class="abs band-go">
      <svg width="28" height="28" viewBox="0 0 28 28"><path d="M11 9l6 5-6 5" fill="none" stroke="#fff" stroke-width="2"/></svg>
    </div>
  </section>

  <main>
    <div class="abs welcome">
      <h2 class="section-title">WELCOME TO MY WEBSITE MAINPAGE</h2>
      <p>Mauris vel lacus vitae felis vestibulum volutpat. Etiam est nunc, venenatis in tristique eu, imperdiet ac nisl. Cum sociis natoque penatibus et magnis dis parturient montes, nascetur ridiculus mus. In iaculis facilisis massa, et aliquam tortor pulvinar nec.</p>
      <p>Praesent vitae lacus mi, sed laoreet neque. Nulla facilisi. Curabitur vel purus quis libero tincidunt rhoncus. Aenean eleifend porttitor nunc, non vehicula quam molestie eget.</p>
    </div>

    <h2 class="abs blog-head accent-title">LATEST BLOG</h2>

    <article class="abs post" style="top:615px">
      <div class="post-thumb" role="img" aria-label="Photo of a businesswoman working at a laptop" style="background:linear-gradient(135deg,#d8dde2,#9ea8b2)"></div>
      <div class="post-body">
        <h3>Mauris vel lacus vitae felis</h3>
        <p>Etiam est nunc, venenatis in tristique eu, imperdiet ac nisl. Cum sociis natoque penatibus et magnis dis parturient montes, nascetur ridiculus mus. In iaculis facilisis massa.</p>
        <span class="read-more">READ MORE »</span>
      </div>
    </article>

    <article class="abs post" style="top:770px">
      <div class="post-thumb" role="img" aria-label="Photo of a team meeting around an office table" style="background:linear-gradient(135deg,#eef0f2,#b8c0c6)"></div>
      <div class="post-body">
        <h3>Mauris vel lacus vitae felis vestibulum volutpat</h3>
        <p>Etiam est nunc, venenatis in tristique eu, imperdiet ac nisl. Cum sociis natoque penatibus et magnis dis parturient montes, nascetur ridiculus mus.</p>
        <span class="read-more">READ MORE »</span>
      </div>
    </article>

    <article class="abs post" style="top:925px">
      <div class="post-thumb" role="img" aria-label="Photo of a woman in a business suit" style="background:linear-gradient(135deg,#e6e2df,#8e8480)"></div>
      <div class="post-body">
        <h3>Pellentesque rutrum malesuada</h3>
        <p>Etiam est nunc, venenatis in tristique eu, imperdiet ac nisl. Cum sociis natoque penatibus et magnis dis parturient montes, nascetur ridiculus mus. In iaculis facilisis massa.</p>
        <span class="read-more">READ MORE »</span>
      </div>
    </article>
  </main>

  <aside>
    <div class="abs side-photo" role="img" aria-label="Portrait photo of the coach"></div>
    <div class="abs about-box">
      <h4>ABOUT ME</h4>
      <p>Mauris vel lacus vitae felis vestibulum volutpat. Etiam est nunc, venenatis in tristique eu, imperdiet ac nisl sociis.</p>
    </div>

    <h3 class="abs gallery-head accent-title">PHOTO GALLERY</h3>
    <div class="abs gallery" role="img" aria-label="Grid of six gallery photos of women at work">
      <span style="background:#d9c9c3"></span><span style="background:#c7b8b1"></span><span style="background:#e2d6cf"></span>
      <span style="background:#bfb2ad"></span><span style="background:#d3c4bc"></span><span style="background:#a8998f"></span>
    </div>

    <h3 class="abs news-head accent-title">NEWSLETTER SIGN UP</h3>
    <p class="abs news-text">Sign up for my latest news</p>
    <div class="abs news-field" style="top:840px">Name</div>
    <div class="abs news-field" style="top:864px">Email</div>
    <div class="abs subscribe">SUBSCRIBE</div>

    <h3 class="abs testi-head accent-title">TESTIMONIALS</h3>
    <p class="abs testi-text">“Mauris vel lacus vitae felis vestibulum volutpat. Etiam est nunc, venenatis in tristique eu, imperdiet ac nisl. Cum sociis natoque penatibus et magnis dis parturient montes nascetur.”</p>
    <div class="abs testi-author">By Author Name</div>
  </aside>

  <footer>
    <div class="abs footer"></div>
    <nav class="abs footer-nav"><span>HOME</span><span>|</span><span>CONSULTING</span><span>|</span><span>COACHING</span><span>|</span><span>BLOG</span><span>|</span><span>GALLERY</span><span>|</span><span>CONTACT</span></nav>
    <div class="abs socials"><span style="background:#4a90d9"></span><span style="background:#3b5fa8"></span><span style="background:#e24a3b"></span><span style="background:#3aa6d8"></span></div>
    <div class="abs copyright-bar"></div>
    <div class="abs copyright">© 2014 Marisel. All Rights Reserved. Designed for you.</div>
  </footer>
</body>
</html>
```